" A empresa ainda é nova e irá trabalhar com projetos e obras para terceiros, estou querendo atuar principalmente em condomínio fechado na construções de casas. "

```html
<!DOCTYPE html>
<html lang="pt-BR">
<head>
<meta charset="utf-8">
<title>Assinatura de e-mail – Norva</title>
<link rel="stylesheet" href="https://fonts.googleapis.com/css2?family=Arimo:wght@400;700&display=swap">
<style>
  :root {
    --page-bg: #eef0f2;
    --navy: #0f2f4a;
    --navy-deep: #0b2740;
    --accent: #2aa7d8;
    --text-light: #e8f1f7;
    --faint: rgba(42, 167, 216, 0.10);
  }
  * { margin: 0; padding: 0; box-sizing: border-box; }
  html, body {
    width: 1200px; height: 1200px; overflow: hidden;
    background: var(--page-bg);
    font-family: "Arimo", Arial, sans-serif;
  }
  .canvas {
    width: 1200px; height: 1200px;
    display: flex; align-items: center; justify-content: center;
  }
  .signature {
    position: relative;
    width: 1000px; height: 256px;
    background: linear-gradient(90deg, var(--navy-deep), var(--navy));
    border-bottom: 12px solid var(--accent);
    border-radius: 6px;
    overflow: hidden;
  }
  .brand {
    position: absolute; left: 120px; top: 78px;
    width: 220px;
    display: flex; flex-direction: column; align-items: center; gap: 8px;
  }
  .brand-row { display: flex; align-items: center; gap: 12px; }
  .brand-square { width: 22px; height: 22px; background: var(--accent); }
  .brand-name {
    font-size: 44px; font-weight: 700; letter-spacing: 3px;
    color: var(--accent); line-height: 1;
  }
  .brand-tagline {
    font-size: 11px; font-weight: 700; letter-spacing: 1.5px;
    color: var(--accent); text-transform: uppercase;
  }
  .contacts {
    position: absolute; left: 380px; width: 320px; top: 46px;
    list-style: none;
  }
  .contact-item {
    display: flex; align-items: center; justify-content: flex-end;
    gap: 20px; height: 41px;
    font-size: 20px; color: var(--text-light);
  }
  .contact-icon { width: 20px; height: 20px; flex: none; }
  .backdrop-mark {
    position: absolute; right: 30px; bottom: 0;
    width: 150px; height: 220px;
    background: var(--faint);
  }
</style>
</head>
<body>
<main class="canvas">
  <section class="signature" aria-label="Assinatura de e-mail Norva">
    <div class="brand">
      <div class="brand-row">
        <span class="brand-square" aria-hidden="true"></span>
        <span class="brand-name">NORVA</span>
      </div>
      <span class="brand-tagline">Projetos e Construções</span>
    </div>

    <ul class="contacts">
      <li class="contact-item">
        <span>contato@norvaobras.com.br</span>
        <svg class="contact-icon" viewBox="0 0 20 20" aria-hidden="true">
          <rect x="2" y="5" width="16" height="11" rx="2" fill="var(--accent)"/>
          <path d="M3 6 L10 11 L17 6" fill="none" stroke="var(--navy)" stroke-width="1.5"/>
        </svg>
      </li>
      <li class="contact-item">
        <span>11 3456-7821</span>
        <svg class="contact-icon" viewBox="0 0 20 20" aria-hidden="true">
          <rect x="5" y="2" width="10" height="16" rx="1.5" fill="none" stroke="var(--accent)" stroke-width="1.8"/>
        </svg>
      </li>
      <li class="contact-item">
        <span>11 98765-4320</span>
        <svg class="contact-icon" viewBox="0 0 20 20" aria-hidden="true">
          <rect x="5" y="1.5" width="10" height="17" rx="2" fill="none" stroke="var(--accent)" stroke-width="1.8"/>
          <circle cx="10" cy="15.5" r="1" fill="var(--accent)"/>
        </svg>
      </li>
      <li class="contact-item">
        <span>Rua das Acácias, 120</span>
        <svg class="contact-icon" viewBox="0 0 20 20" aria-hidden="true">
          <path d="M10 19 C6 13 4 10 4 7.5 A6 6 0 0 1 16 7.5 C16 10 14 13 10 19 Z" fill="var(--accent)"/>
          <circle cx="10" cy="7.5" r="2.2" fill="var(--navy)"/>
        </svg>
      </li>
    </ul>

    <div class="backdrop-mark" aria-hidden="true"></div>
  </section>
</main>
</body>
</html>
```